palduro.org business card design

We need 2-sided business cards for palduro.org; one side will be printed in English (EN), the other in Spanish (ES); the information represnted will be the same.
We are a non-profit that aims to mentor and coach future leaders / visionaries. Our target markets are developing countries (Latin America, Africa, Asia) rather than the developed ("western") world. Our business model works by finding funding to mentor / coach a candidate. We provide several mentors / coaches per candidate which help translate the candidate's vision / dream into a path with objectives and steps.
We want the business cards to transmit our values, which are: innovation, learning / self-improvement, equality (i.e. free from discrimination), boldness, intelligence, thoughtfulness, culture, society, future, sustainability.
We recommend the designers work with these values to produce a bold and innovative design, which does not need to adhere to the traditional criteria for business cards. Please use fresh (modern) colours.

Target Market(s)

Visionaries and thought leaders all over the world, but initially in Latin America. We don't discriminate on age, sex, religion, race or any other difference between people

Industry/Entity Type

Leadership

Contact Information for Business Card

The business cards will contain one language (English / Spanish) per side. It would be nice to have some continuity between the front and the back (e.g. pattern, colours).
Each side will contain the company name, website (www.palduro.org) and a slogan / mantra (which will be provided and can be represented as a placeholder until such time). The other details will be Name, (Function), and contact details (email and phone number).

Font styles to use
Sans Serif

Colors

Designer to choose colors to be used in the design.

Requirements
Must have
• [Side A: ENGLISH --- COMPANY INFO]
• [Company Name] Palduro
• [Slogan / Mantra] Build your path!
• [Website] palduro.org
• [Side A: ENGLISH --- PERSONAL INFO]
• [Name] Tim Hallox
• [Job Title] Mentoring Coordinator
• [Phone / WhatsApp] +51 917 208 386
• [eMail] tim@palduro.org
• [Side B: SPANISH --- COMPANY INFO]
• [Company Name] Palduro
• [Slogan / Mantra] ¡Moldea tu mundo!
• [Website] palduro.org
• [Side B: SPANISH --- PERSONAL INFO]
• [Name] Timothy Hallox
• [Job Title] Coordinador de Mentoreo
• [eMail] tim@palduro.org
• [SIDE A: ENGLISH --- Central Values]
• - Future
• - Growth
• - Leadership
• [SIDE B: SPANISH --- Central Values]
• - Futuro
• - Liderazgo
• - Crecimiento
Nice to have
• Innovative and different design. Modern and fresh. Bold and clever.
• Secondary Values (we would like represented) are:
• [SIDE A: ENGLISH --- Secondary Values]
• - Equality
• - Innovation
• - Sustainability
• [SIDE B: SPANISH --- Secondary Values]
• - Igualdad
• - Innovación
• - Sostenibilidad
Should not have
• Please note that the images I have attached to this brief are just some images that I liked while browsing for material for the website. It does not imply I want these colours or this type of design, just that I felt these images had a good feel.

```html
<!DOCTYPE html>
<html lang="en">
<head>
<meta charset="utf-8">
<title>Palduro business cards</title>
<link rel="stylesheet" href="https://fonts.googleapis.com/css2?family=Jost:wght@300;400;500;600;700;800&display=swap">
<style>
  :root {
    --green: #52aa89;
    --coral: #d9684e;
    --orange: #f29322;
    --white: #ffffff;
    --rule: #e4e4e4;
  }
  * { box-sizing: border-box; margin: 0; padding: 0; }
  html, body { width: 1110px; height: 1200px; overflow: hidden; background: var(--white); }
  body { position: relative; font-family: "Jost", sans-serif; }

  .card { position: absolute; left: 0; }
  .card--en { top: 0; width: 873px; height: 495px; }
  .card--es { top: 612px; width: 895px; height: 506px; }

  .card__face { position: absolute; left: 0; top: 0; width: 100%; }
  .card--en .card__face { height: 415px; background: var(--green); }
  .card--es .card__face { height: 425px; background: var(--coral); }

  .holder { position: absolute; color: var(--white); }
  .holder__name { font-weight: 700; font-size: 36px; letter-spacing: 4px; line-height: 1; }
  .holder__role { font-weight: 400; font-size: 22px; letter-spacing: 2.6px; margin-top: 12px; line-height: 1.1; }
  .card--en .holder { left: 67px; top: 44px; }
  .card--es .holder { left: 69px; top: 46px; }
  .card--es .holder__role { margin-left: 4px; }

  .value { position: absolute; width: 200px; text-align: center; }
  .value__badge { width: 100px; height: 100px; border-radius: 50%; background: var(--white); margin: 0 auto; display: flex; align-items: center; justify-content: center; }
  .value__badge svg { width: 58px; height: 58px; }
  .value__label { color: var(--white); font-weight: 800; font-size: 20px; letter-spacing: 2px; margin-top: 6px; line-height: 1.1; }
  .card--en .value__badge { color: var(--orange); }
  .card--es .value__badge { color: var(--green); }

  .contacts { position: absolute; list-style: none; }
  .card--en .contacts { left: 485px; top: 153px; }
  .card--es .contacts { left: 497px; top: 158px; }
  .contacts li { display: flex; align-items: center; height: 50px; margin-bottom: 15px; color: var(--white); font-size: 30px; font-weight: 400; letter-spacing: 0.5px; }
  .contacts__icon { width: 50px; height: 50px; border-radius: 50%; background: var(--white); display: flex; align-items: center; justify-content: center; margin-right: 10px; flex-shrink: 0; }
  .contacts__icon svg { width: 30px; height: 30px; }
  .card--en .contacts__icon { color: var(--green); }
  .card--es .contacts__icon { color: var(--coral); }
  .contacts__icon--web svg { width: 44px; height: 44px; }

  .card__footer { position: absolute; left: 0; bottom: 0; width: 100%; background: var(--white); border: 1px solid var(--rule); border-top: none; display: flex; align-items: center; }
  .card--en .card__footer { height: 80px; color: var(--orange); }
  .card--es .card__footer { height: 81px; color: var(--green); }
  .brand { font-size: 38px; letter-spacing: 5px; text-align: center; line-height: 1; }
  .card--en .brand { width: 403px; font-weight: 600; }
  .card--es .brand { width: 413px; font-weight: 500; }
  .divider { width: 2px; align-self: stretch; margin: 8px 0 4px; }
  .card--en .divider { background: var(--orange); }
  .card--es .divider { background: var(--green); }
  .slogan { flex: 1; text-align: center; font-size: 29px; letter-spacing: 4px; line-height: 1; }
  .card--en .slogan { font-weight: 700; }
  .card--es .slogan { font-weight: 600; }
</style>
</head>
<body>

<svg width="0" height="0" style="position:absolute" aria-hidden="true">
  <defs>
    <symbol id="icon-future" viewBox="0 0 60 60">
      <g fill="none" stroke="currentColor" stroke-width="3.5" stroke-linecap="round">
        <path d="M44 14 A24 24 0 1 0 30 54"/>
        <path d="M40 8 L45 14 L38 17"/>
        <path d="M24 20 V34 H32"/>
        <path d="M40 44 c-3-5-10-5-10 0 s7 5 10 0 c3-5 10-5 10 0 s-7 5-10 0z"/>
      </g>
    </symbol>
    <symbol id="icon-growth" viewBox="0 0 60 60">
      <g fill="none" stroke="currentColor" stroke-width="3.5" stroke-linecap="round" stroke-linejoin="round">
        <path d="M8 6 V52 H54"/>
        <path d="M14 42 L26 28 L34 36 L50 18"/>
        <path d="M40 16 H51 V27"/>
      </g>
    </symbol>
    <symbol id="icon-leadership" viewBox="0 0 60 60">
      <g fill="none" stroke="currentColor" stroke-width="2.8" stroke-linecap="round">
        <circle cx="30" cy="8" r="4"/><path d="M25 20 a5 5 0 0 1 10 0"/>
        <path d="M30 22 V30 M12 30 H48 M12 30 V36 M30 30 V36 M48 30 V36"/>
        <circle cx="12" cy="41" r="3.5"/><path d="M7 53 a5 5 0 0 1 10 0"/>
        <circle cx="30" cy="41" r="3.5"/><path d="M25 53 a5 5 0 0 1 10 0"/>
        <circle cx="48" cy="41" r="3.5"/><path d="M43 53 a5 5 0 0 1 10 0"/>
      </g>
    </symbol>
    <symbol id="icon-web" viewBox="0 0 44 44">
      <text x="22" y="25" text-anchor="middle" font-family="Jost, sans-serif" font-size="14" font-weight="500" fill="currentColor">www</text>
      <path d="M25 29 L31 35 M25 29 V33 M25 29 H29" stroke="currentColor" stroke-width="1.8" fill="none" stroke-linecap="round"/>
    </symbol>
    <symbol id="icon-mail" viewBox="0 0 30 30">
      <rect x="3" y="7" width="24" height="17" rx="1.5" fill="currentColor"/>
      <path d="M4 8.5 L15 16.5 L26 8.5" fill="none" stroke="#fff" stroke-width="2"/>
    </symbol>
    <symbol id="icon-phone" viewBox="0 0 30 30">
      <path d="M8 3 L12 3 L14 10 L10.5 12.5 C12 16.5 14 18.5 17.5 19.5 L20 16 L27 18 L27 22 C27 25 24 27 21 26.5 C11 24.5 5.5 19 3.5 9 C3 6 5 3 8 3Z" fill="currentColor"/>
    </symbol>
  </defs>
</svg>

<section class="card card--en" lang="en">
  <div class="card__face">
    <div class="holder">
      <h1 class="holder__name">TIM HALLOX</h1>
      <p class="holder__role">mentoring coordinator</p>
    </div>

    <div class="value" style="left:-5px; top:137px;">
      <div class="value__badge"><svg><use href="#icon-future"/></svg></div>
      <p class="value__label">future</p>
    </div>
    <div class="value" style="left:162px; top:135px;">
      <div class="value__badge"><svg><use href="#icon-growth"/></svg></div>
      <p class="value__label">growth</p>
    </div>
    <div class="value" style="left:70px; top:275px;">
      <div class="value__badge"><svg><use href="#icon-leadership"/></svg></div>
      <p class="value__label">leadership</p>
    </div>

    <ul class="contacts">
      <li><span class="contacts__icon contacts__icon--web"><svg><use href="#icon-web"/></svg></span>palduro.org</li>
      <li><span class="contacts__icon"><svg><use href="#icon-mail"/></svg></span>tim@palduro.org</li>
      <li><span class="contacts__icon"><svg><use href="#icon-phone"/></svg></span>+51 917 208 386</li>
    </ul>
  </div>
  <footer class="card__footer">
    <p class="brand">PALDURO</p>
    <span class="divider"></span>
    <p class="slogan">Build your path!</p>
  </footer>
</section>

<section class="card card--es" lang="es">
  <div class="card__face">
    <div class="holder">
      <h2 class="holder__name">TIM HALLOX</h2>
      <p class="holder__role">coordinador de mentoreo</p>
    </div>

    <div class="value" style="left:-2px; top:140px;">
      <div class="value__badge"><svg><use href="#icon-future"/></svg></div>
      <p class="value__label">futuro</p>
    </div>
    <div class="value" style="left:168px; top:138px;">
      <div class="value__badge"><svg><use href="#icon-growth"/></svg></div>
      <p class="value__label">liderazgo</p>
    </div>
    <div class="value" style="left:75px; top:282px;">
      <div class="value__badge"><svg><use href="#icon-leadership"/></svg></div>
      <p class="value__label">crecimiento</p>
    </div>

    <ul class="contacts">
      <li><span class="contacts__icon contacts__icon--web"><svg><use href="#icon-web"/></svg></span>palduro.org</li>
      <li><span class="contacts__icon"><svg><use href="#icon-mail"/></svg></span>tim@palduro.org</li>
      <li><span class="contacts__icon"><svg><use href="#icon-phone"/></svg></span>+51 917 208 386</li>
    </ul>
  </div>
  <footer class="card__footer">
    <p class="brand">PALDURO</p>
    <span class="divider"></span>
    <p class="slogan">Build your path!</p>
  </footer>
</section>

</body>
</html>
```